Poster for a online company that buys your stuff

SwapHollow offers a website which customers can get a instant offer for stuff their looking to sell. They then Courier the items in to us and they get paid the same day it arrives
We're looking for an eye catching design which portrays our hassle free process
We'll need your help to come up with a slogan/catch phrase and our easy 1,2,3 process so customers can see the poster and instantly have a clear understanding of what we do
1. Get an instant offer on our website
2. Send your item(s) to us
3.Get paid within 24 Hours
Industry/Entity Type
It Company
Look and feel
Each slider illustrates characteristics of the customer's brand and the style your logo design should communicate.

```html
<!DOCTYPE html>
<html lang="en">
<head>
<meta charset="utf-8">
<title>SwapHollow – Sell your products easily</title>
<link rel="stylesheet" href="https://fonts.googleapis.com/css2?family=Arimo:wght@400;700&display=swap">
<style>
  :root{
    --backdrop:#6b6b6b;
    --paper:#eef0ef;
    --ink:#2b2b2b;
    --forest:#065a35;
    --leaf:#0f9a45;
    --grass:#5cb85c;
    --mint:#cfe3a0;
    --lime:#8dc63f;
    --badge:#3a3533;
    --white:#ffffff;
    --cta:#169a36;
    --cta-line:#1fb23f;
  }
  *{margin:0;padding:0;box-sizing:border-box}
  html,body{width:900px;height:1200px;overflow:hidden}
  body{background:var(--backdrop);font-family:"Arimo",Arial,sans-serif;position:relative}
  .poster{position:absolute;left:135px;top:155px;width:645px;height:913px;background:var(--paper);overflow:hidden}
  .poster-waves{position:absolute;left:0;top:0;width:645px;height:913px}
  .mascot-area{position:absolute;left:175px;top:25px;width:325px;height:285px;border-radius:40px;
    background:radial-gradient(circle at 45% 40%,#a9d14e 0%,#7fb93a 45%,#f0a21c 100%);opacity:.85}
  .brand-name{position:absolute;left:0;top:298px;width:610px;text-align:center;font-weight:700;font-size:50px;color:var(--ink);letter-spacing:-1px}
  .headline{position:absolute;left:0;width:645px;text-align:center;color:var(--paper)}
  .headline--lead{top:482px;font-size:28px;letter-spacing:.5px}
  .headline--main{top:510px;font-size:84px;letter-spacing:7px;line-height:1}
  .headline--sub{top:600px;font-size:31px;font-weight:700}
  .steps{position:absolute;left:0;top:630px;width:645px;height:180px}
  .step-caption{position:absolute;top:794px;width:180px;text-align:center;color:var(--white);font-size:14px;line-height:17px}
  .step-caption--one{left:53px}
  .step-caption--two{left:242px}
  .step-caption--three{left:427px}
  .call-bar{position:absolute;left:0;top:853px;width:645px;height:60px}
  .call-label{position:absolute;left:40px;top:857px;font-size:41px;color:var(--white)}
  .call-number{position:absolute;left:260px;top:858px;font-size:38px;font-weight:700;color:var(--white);letter-spacing:.5px}
</style>
</head>
<body>
<main class="poster">
  <svg class="poster-waves" viewBox="0 0 645 913" aria-hidden="true">
    <path d="M0,460 Q300,330 645,440 L645,913 L0,913 Z" fill="var(--mint)"/>
    <path d="M0,482 Q290,350 645,456 L645,913 L0,913 Z" fill="var(--grass)"/>
    <path d="M0,505 Q330,372 645,475 L645,913 L0,913 Z" fill="var(--leaf)"/>
    <path d="M0,545 Q330,400 645,540 L645,913 L0,913 Z" fill="var(--forest)"/>
  </svg>

  <div class="mascot-area" role="img" aria-label="Cartoon courier mascot in green cap and overalls giving a thumbs up while carrying an orange parcel"></div>
  <div class="brand-name">SwapHollow</div>

  <p class="headline headline--lead">SELL YOUR PRODUCTS</p>
  <p class="headline headline--main">EASILY</p>
  <p class="headline headline--sub">IN 3 SIMPLE STEPS</p>

  <svg class="steps" viewBox="0 630 645 180" aria-hidden="true">
    <g stroke="var(--leaf)" stroke-width="1.5" fill="none">
      <path d="M328,635 V665 M137,665 H520 M137,665 V690 M520,665 V690"/>
    </g>
    <g font-family="Arimo, Arial, sans-serif" font-size="21" fill="var(--white)">
      <text x="84" y="713">1</text>
      <text x="266" y="713">2</text>
      <text x="450" y="713">3</text>
    </g>
    <!-- step 1: globe -->
    <circle cx="143" cy="738" r="48" fill="var(--lime)"/>
    <circle cx="143" cy="738" r="40" fill="var(--badge)"/>
    <g stroke="var(--white)" stroke-width="2" fill="none">
      <circle cx="143" cy="738" r="22"/>
      <ellipse cx="143" cy="738" rx="10" ry="22"/>
      <path d="M121,738 H165 M143,716 V760 M125,726 H161 M125,750 H161"/>
    </g>
    <!-- step 2: trolley -->
    <circle cx="332" cy="738" r="48" fill="var(--lime)"/>
    <circle cx="332" cy="738" r="40" fill="var(--badge)"/>
    <g stroke="var(--white)" stroke-width="2" fill="none">
      <path d="M312,718 H317 V754 H354"/>
      <rect x="322" y="724" width="26" height="24"/>
      <path d="M330,724 V748 M340,724 V748"/>
      <circle cx="320" cy="759" r="3"/>
      <circle cx="350" cy="759" r="3"/>
    </g>
    <!-- step 3: 24h payment -->
    <circle cx="517" cy="738" r="48" fill="var(--lime)"/>
    <circle cx="517" cy="738" r="40" fill="var(--badge)"/>
    <g stroke="var(--white)" stroke-width="3" fill="none">
      <path d="M503,722 A22,22 0 1 1 500,752"/>
    </g>
    <path d="M496,716 L507,720 L500,728 Z" fill="var(--white)"/>
    <g fill="var(--white)" font-family="Arimo, Arial, sans-serif" font-weight="700">
      <text x="514" y="733" font-size="15">P</text>
      <text x="490" y="752" font-size="17">24h</text>
    </g>
  </svg>

  <p class="step-caption step-caption--one">Get an instant<br>offer on our website</p>
  <p class="step-caption step-caption--two">Send your<br>item(s) to us</p>
  <p class="step-caption step-caption--three">Get paid<br>within 24 Hours</p>

  <svg class="call-bar" viewBox="0 853 645 60" aria-hidden="true">
    <rect x="0" y="853" width="645" height="60" fill="var(--forest)"/>
    <path d="M0,853 H205 L240,905 H0 Z" fill="var(--cta)"/>
    <rect x="0" y="905" width="645" height="8" fill="var(--cta-line)"/>
  </svg>
  <p class="call-label">Call us:</p>
  <p class="call-number">077- 4812- 6630</p>
</main>
</body>
</html>
```